Stationary design for new digital markerting company

I need a stationary design for a new digital marketing company called Mossy Otter.
We work with businesses to help them create and increase their online presence in order to increase awareness of their brand.
The design must keep with the colour schemes of our logo.
I would like a design that stands out but isn't over the top while also being professional and sophisticated.

Target Market(s)

other businesses

Industry/Entity Type

Business Consultant

Font styles to use
Sans Serif

Colors
abd036
ffffff
a54499

Requirements
Must have
• logo, plus the same colour scheme

```html
<!DOCTYPE html>
<html lang="en">
<head>
<meta charset="utf-8">
<title>Mossy Otter Stationery</title>
<link rel="stylesheet" href="https://fonts.googleapis.com/css2?family=Montserrat:wght@400;500;600;700&display=swap">
<style>
  :root {
    --green: #abd036;
    --green-deep: #7fbf1e;
    --magenta: #a54499;
    --magenta-deep: #a31f7e;
    --white: #ffffff;
    --paper: #f7f7f7;
    --ink: #5b5b5b;
    --stage: #d9d9d9;
  }
  * { margin: 0; padding: 0; box-sizing: border-box; }
  html, body { width: 1200px; height: 900px; overflow: hidden; }
  body {
    background: var(--stage);
    font-family: "Montserrat", sans-serif;
    color: var(--ink);
    position: relative;
  }
  .sheet { position: absolute; overflow: hidden; }
  .paper { background: var(--paper); }
  .solid { background: var(--magenta-deep); }

  .mark { position: absolute; border-radius: 50%; background: var(--green-deep); }
  .brand-name {
    position: absolute; font-weight: 600; letter-spacing: 0.04em;
    text-transform: uppercase; white-space: nowrap; line-height: 1;
  }
  .brand-name.on-light { color: var(--magenta-deep); }
  .brand-name.on-dark { color: var(--white); }
  .tagline {
    position: absolute; white-space: nowrap; line-height: 1;
    letter-spacing: 0.28em; font-weight: 500;
  }
  .tagline.on-light { color: #555; }
  .tagline.on-dark { color: var(--white); }
  .wave { position: absolute; left: 0; bottom: 0; width: 100%; display: block; }

  /* Letterhead */
  .letterhead { left: 220px; top: 54px; width: 382px; height: 539px; }
  .letterhead .mark { left: 76px; top: 17px; width: 38px; height: 38px; }
  .letterhead .brand-name { left: 35px; top: 79px; font-size: 13px; }
  .letterhead .tagline { left: 36px; top: 94px; font-size: 4.6px; }
  .contact-block { position: absolute; left: 280px; top: 44px; font-size: 4.8px; line-height: 6.6px; color: #444; }
  .contact-row { display: flex; align-items: center; gap: 3px; }
  .contact-icon { width: 5px; height: 5px; background: var(--green-deep); border-radius: 1px; display: inline-block; }
  .contact-block .address { margin-top: 4px; }
  .letter-body {
    position: absolute; left: 35px; top: 182px; width: 311px;
    font-size: 5.4px; line-height: 7px; color: #666; text-align: justify;
  }
  .letter-body p { margin-bottom: 6px; }
  .letter-body .salutation { font-weight: 700; color: #444; margin-bottom: 8px; }
  .sign-off { position: absolute; left: 35px; top: 395px; font-size: 5.4px; line-height: 7px; color: #666; }
  .sign-off .signer { font-weight: 700; color: #444; }
  .signature { position: absolute; left: 85px; top: 385px; width: 80px; height: 38px; background: linear-gradient(90deg, rgba(90,110,200,0.12), rgba(90,110,200,0.25)); border-radius: 4px; }

  /* Folder */
  .folder { left: 650px; top: 40px; width: 415px; height: 553px; border-radius: 3px; }
  .folder .spine { position: absolute; left: 24px; top: 0; width: 2px; height: 100%; background: rgba(0,0,0,0.08); }
  .folder .mark { left: 181px; top: 74px; width: 54px; height: 54px; }
  .folder .brand-name { left: 0; width: 100%; text-align: center; top: 135px; font-size: 20px; }
  .folder .tagline { left: 0; width: 100%; text-align: center; top: 152px; font-size: 7px; }
  .folder .site { position: absolute; left: 0; width: 100%; text-align: center; top: 520px; font-size: 8.5px; color: var(--white); letter-spacing: 0.04em; }

  /* Business cards */
  .card-front { left: 79px; top: 638px; width: 163px; height: 90px; }
  .card-front .mark { left: 34px; top: 23px; width: 21px; height: 21px; }
  .card-front .brand-name { left: 11px; top: 52px; font-size: 8px; }
  .card-front .tagline { left: 11px; top: 62px; font-size: 3px; letter-spacing: 0.22em; }
  .card-front .divider { position: absolute; left: 91px; top: 19px; width: 0.6px; height: 52px; background: #ccc; }
  .card-details { position: absolute; left: 101px; top: 20px; font-size: 3.6px; line-height: 4.8px; color: #444; }
  .card-details .person { font-size: 4.6px; font-weight: 700; color: var(--magenta-deep); text-transform: uppercase; }
  .card-details .role { margin-bottom: 4px; }
  .card-details .contact-icon { width: 3.4px; height: 3.4px; }
  .card-details .contact-row { gap: 2px; }
  .card-details .address { margin-top: 2px; }

  .card-back { left: 79px; top: 748px; width: 163px; height: 91px; }
  .card-back .mark { left: 72px; top: 27px; width: 20px; height: 20px; }
  .card-back .brand-name { left: 0; width: 100%; text-align: center; top: 52px; font-size: 8px; }
  .card-back .tagline { left: 0; width: 100%; text-align: center; top: 61px; font-size: 3px; letter-spacing: 0.22em; }

  /* Envelopes */
  .envelope-front { left: 278px; top: 640px; width: 400px; height: 199px; }
  .envelope-front .mark { left: 52px; top: 16px; width: 29px; height: 29px; }
  .envelope-front .brand-name { left: 20px; top: 51px; font-size: 11.5px; }
  .envelope-front .tagline { left: 21px; top: 64px; font-size: 3.8px; }
  .envelope-front .address { position: absolute; left: 36px; top: 76px; font-size: 5px; line-height: 6.6px; color: #444; text-align: center; }

  .envelope-back { left: 724px; top: 640px; width: 399px; height: 199px; background: var(--paper); }
  .envelope-back .flap { position: absolute; left: 0; top: 0; width: 100%; height: 56px; display: block; }
  .envelope-back .mark { left: 191px; top: 21px; width: 17px; height: 17px; }
</style>
</head>
<body>

  <!-- Letterhead -->
  <section class="sheet paper letterhead">
    <span class="mark"></span>
    <div class="brand-name on-light">Mossy Otter</div>
    <div class="tagline on-light">Growing Your Online Reach</div>

    <div class="contact-block">
      <div class="contact-row"><span class="contact-icon"></span>1300 555 018</div>
      <div class="contact-row"><span class="contact-icon"></span>info@mossyotter.com</div>
      <div class="contact-row"><span class="contact-icon"></span>www.mossyotter.com</div>
      <div class="address">Level 12, Harbour Point<br>88 Wattle Street, Sydney</div>
    </div>

    <div class="letter-body">
      <p class="salutation">Dear sir,</p>
      <p>Our studio helps growing businesses build a clear and steady presence online. We plan campaigns, shape content and track results so every step of the work can be measured. Good marketing starts with listening, and we take time to understand your goals before suggesting any direction.</p>
      <p>In a busy market, attention is hard to earn and easy to lose. That is why we focus on search visibility, social channels and useful content that gives people a reason to stay. Each plan is built around your audience, your budget and the pace that suits your team.</p>
      <p>We report plainly and often, so you always know what is working and what we will change next. Small gains add up over time and a consistent voice helps your brand be remembered.</p>
      <p>We would welcome the chance to talk about your plans and show how we can support your growth this year.</p>
    </div>

    <div class="sign-off">Yours Sincerely,<br><span class="signer">Jonah Keller</span></div>
    <div class="signature" role="img" aria-label="Handwritten signature of Jonah Keller"></div>

    <svg class="wave" viewBox="0 0 400 30" height="30" preserveAspectRatio="none" aria-hidden="true">
      <path d="M0,16 C110,2 250,0 400,12 L400,30 L0,30 Z" fill="var(--green-deep)"/>
      <path d="M0,22 C120,8 250,6 400,18 L400,30 L0,30 Z" fill="#e4e4e4"/>
      <path d="M0,30 C80,22 170,12 270,16 C330,19 370,24 400,26 L400,30 Z" fill="var(--magenta-deep)"/>
    </svg>
  </section>

  <!-- Folder -->
  <section class="sheet solid folder">
    <span class="spine"></span>
    <span class="mark"></span>
    <div class="brand-name on-dark">Mossy Otter</div>
    <div class="tagline on-dark">Growing Your Online Reach</div>
    <div class="site">www.mossyotter.com</div>
  </section>

  <!-- Business card front -->
  <section class="sheet paper card-front">
    <span class="mark"></span>
    <div class="brand-name on-light">Mossy Otter</div>
    <div class="tagline on-light">Growing Your Online Reach</div>
    <span class="divider"></span>
    <div class="card-details">
      <div class="person">Priya Lindqvist</div>
      <div class="role">Managing Director</div>
      <div class="contact-row"><span class="contact-icon"></span>1300 555 018</div>
      <div class="contact-row"><span class="contact-icon"></span>info@mossyotter.com</div>
      <div class="contact-row"><span class="contact-icon"></span>www.mossyotter.com</div>
      <div class="address">Level 12, Harbour Point<br>88 Wattle Street, Sydney</div>
    </div>
    <svg class="wave" viewBox="0 0 400 40" height="14" preserveAspectRatio="none" aria-hidden="true">
      <path d="M0,18 C110,2 250,0 400,16 L400,40 L0,40 Z" fill="var(--green-deep)"/>
      <path d="M0,26 C120,10 250,8 400,24 L400,40 L0,40 Z" fill="#e4e4e4"/>
      <path d="M0,40 C80,30 170,16 270,20 C330,24 370,30 400,34 L400,40 Z" fill="var(--magenta-deep)"/>
    </svg>
  </section>

  <!-- Business card back -->
  <section class="sheet solid card-back">
    <span class="mark"></span>
    <div class="brand-name on-dark">Mossy Otter</div>
    <div class="tagline on-dark">Growing Your Online Reach</div>
  </section>

  <!-- Envelope front -->
  <section class="sheet paper envelope-front">
    <span class="mark"></span>
    <div class="brand-name on-light">Mossy Otter</div>
    <div class="tagline on-light">Growing Your Online Reach</div>
    <div class="address">Level 12, Harbour Point<br>88 Wattle Street, Sydney</div>
    <svg class="wave" viewBox="0 0 400 30" height="26" preserveAspectRatio="none" aria-hidden="true">
      <path d="M0,16 C110,2 250,0 400,14 L400,30 L0,30 Z" fill="var(--green-deep)"/>
      <path d="M0,22 C120,8 250,6 400,20 L400,30 L0,30 Z" fill="#e4e4e4"/>
      <path d="M0,30 C80,22 170,10 270,14 C330,18 370,24 400,28 L400,30 Z" fill="var(--magenta-deep)"/>
    </svg>
  </section>

  <!-- Envelope back -->
  <section class="sheet envelope-back">
    <svg class="flap" viewBox="0 0 399 56" preserveAspectRatio="none" aria-hidden="true">
      <path d="M0,0 L399,0 L385,56 L14,56 Z" fill="var(--magenta-deep)"/>
    </svg>
    <span class="mark"></span>
  </section>

</body>
</html>
```